Willowmere Loft B&B Business Card

This beautiful high-class B&B is looking for a business card that stands out from the rest. They are in the middle of the countryside, have chickens, geese and a dog. They also love bumble bees.

I was maybe thinking a rustic drawing / print of a bumble bee and a sketch of the house, I am not sure.. I quite like the feel of this... http://www.tarnwick-mill.co.uk/

Industry/Entity Type

Business

Contact Information for Business Card

Willowmere Loft
Bed & Breakfast
Brackleford, Hensworth, Somerset, TA14 7QP
01632 960418 | www.willowmereloft.co.uk

```html
<!DOCTYPE html>
<html lang="en">
<head>
<meta charset="utf-8">
<title>Willowmere Loft B&amp;B – Business Card</title>
<link rel="stylesheet" href="https://fonts.googleapis.com/css2?family=Cinzel:wght@400&family=Libre+Caslon+Condensed:wght@500&display=swap">
<style>
  :root {
    --page: #ececec;
    --card: #ffffff;
    --ink: #9c8074;
    --frame: #c9b5ab;
    --sky: #f4eee9;
    --stone: #e9e1d8;
    --roof: #b98f86;
    --path: #e6dcd2;
    --grass: #8f8d6b;
    --grass-dark: #6f6a52;
  }
  * { margin: 0; padding: 0; box-sizing: border-box; }
  html, body { width: 1200px; height: 1200px; overflow: hidden; background: var(--page); }
  .canvas { position: relative; width: 1200px; height: 1200px; }

  .card {
    position: absolute; left: 158px; width: 888px; height: 526px;
    background: var(--card); overflow: hidden;
  }
  .card--front { top: 50px; }
  .card--back { top: 613px; }

  .scene {
    position: absolute; top: 0; height: 100%;
    background:
      linear-gradient(to bottom, var(--sky) 0%, var(--sky) 22%, var(--roof) 30%, var(--stone) 38%, var(--stone) 62%, var(--path) 72%, var(--grass) 88%, var(--grass-dark) 100%);
    opacity: .85;
  }
  .card--front .scene {
    left: 0; width: 520px;
    -webkit-mask-image: linear-gradient(to right, #000 62%, transparent 100%);
            mask-image: linear-gradient(to right, #000 62%, transparent 100%);
  }
  .card--back .scene { width: 380px; top: 60px; height: 466px; opacity: .7; }
  .card--back .scene--left {
    left: 0;
    -webkit-mask-image: linear-gradient(to right, #000 45%, transparent 100%);
            mask-image: linear-gradient(to right, #000 45%, transparent 100%);
  }
  .card--back .scene--right {
    right: 0;
    -webkit-mask-image: linear-gradient(to left, #000 45%, transparent 100%);
            mask-image: linear-gradient(to left, #000 45%, transparent 100%);
  }

  .nameplate {
    position: absolute; border: 1px solid var(--frame);
    display: flex; flex-direction: column; justify-content: center;
    padding-left: 24px; color: var(--ink);
  }
  .card--front .nameplate { left: 462px; top: 184px; width: 374px; height: 156px; }
  .card--back .nameplate { left: 280px; top: 58px; width: 327px; height: 131px; padding-left: 28px; }

  .nameplate__title {
    font-family: "Cinzel", serif; font-weight: 400; line-height: 1.08;
    letter-spacing: .02em;
  }
  .card--front .nameplate__title { font-size: 37px; }
  .card--back .nameplate__title { font-size: 32px; }
  .nameplate__line { display: flex; align-items: baseline; gap: 12px; }
  .nameplate__tag {
    font-family: "Libre Caslon Condensed", serif; font-weight: 500;
    color: var(--ink);
  }
  .card--front .nameplate__tag { font-size: 26px; }
  .card--back .nameplate__tag { font-size: 23px; }

  .contact {
    position: absolute; left: 0; width: 100%; text-align: center;
    font-family: "Libre Caslon Condensed", serif; font-weight: 500; color: var(--ink);
  }
  .contact__address { top: 212px; font-size: 21px; line-height: 29px; }
  .contact__phone { top: 276px; font-size: 26px; }
  .contact__web { top: 450px; font-size: 19px; }

  .poultry {
    position: absolute; left: 366px; top: 343px; width: 148px; height: 88px;
    background: radial-gradient(ellipse at center, #cdbfb4 0%, #e6ddd6 45%, rgba(255,255,255,0) 72%);
  }
</style>
</head>
<body>
<main class="canvas">
  <section class="card card--front" aria-label="Card front">
    <div class="scene" role="img" aria-label="Soft pencil sketch of the stone barn house with tiled roof, gravel drive and grass"></div>
    <div class="nameplate">
      <div class="nameplate__title">Willowmere</div>
      <div class="nameplate__line">
        <span class="nameplate__title">Loft</span>
        <span class="nameplate__tag">Bed &amp; Breakfast</span>
      </div>
    </div>
  </section>

  <section class="card card--back" aria-label="Card back">
    <div class="scene scene--left" role="img" aria-label="Faded sketch of the barn house, left side"></div>
    <div class="scene scene--right" role="img" aria-label="Faded sketch of the barn house, mirrored on the right"></div>
    <div class="nameplate">
      <div class="nameplate__title">Willowmere</div>
      <div class="nameplate__line">
        <span class="nameplate__title">Loft</span>
        <span class="nameplate__tag">Bed &amp; Breakfast</span>
      </div>
    </div>
    <p class="contact contact__address">Brackleford, Hensworth, Somerset,<br>TA14 7QP</p>
    <p class="contact contact__phone">01632 960418</p>
    <div class="poultry" role="img" aria-label="Soft sketch of two hens"></div>
    <p class="contact contact__web">www.willowmereloft.co.uk</p>
  </section>
</main>
</body>
</html>
```